Seven Quiet Rooms Poster

Seven Quiet Rooms is reaching out to designers, creatives and fans alike to help create an exciting new poster for the film as part of our Fundvaro campaign.

Seven Quiet Rooms is a multi-protagonist, multicultural, humanist drama inspired by the 2008 Mumbai terrorist attacks. Centering on a group of international tourists trapped in their hotel by Islamic fundamentalists, the film aims to explore the key issues facing our society, concerning atheism, religion, religious extremism and humanism.

The film’s poster will be a critical part of a film’s publicity and marketing portfolio and an important resource for the film to take into our festival campaign and distribution talks. We’re looking for a highly polished design that accurately represents the film and matches the standard of the finished film.

We will be uploading some of the best entries to our Chatterbox page for fans to vote on. If you do not wish for your design to appear on the page, please contact us.

You can find our teaser trailer on the Fundvaro link below. We’ve also provided some reference images (found here: http://lnk.example-short.net/Rk4WpZ) and also stills from the film to provide inspiration (found here: http://lnk.example-short.net/Tm8QvB) - how or if you use them is up to you.

Good luck and get designing!

http://www.fundvaro-example.com/projects/seven-quiet-rooms

Please note: Amber Tide Pictures reserves the right to select all promotional material for theatrical release.

Requirements
Must have
• Size: 27" x 40"
Should not have
• Please do not include the credit block on your designs.

```html
<!DOCTYPE html>
<html lang="en">
<head>
<meta charset="utf-8">
<title>Seven Quiet Rooms</title>
<link rel="stylesheet" href="https://fonts.googleapis.com/css2?family=Cinzel:wght@400&display=swap">
<style>
  :root {
    --ink: #0a0808;
    --haze: #cfdde2;
    --steel: #7f9aa3;
    --glow: #f4f8f8;
    --ember: #c9822e;
    --title: #ffffff;
  }
  html, body {
    margin: 0;
    padding: 0;
    width: 809px;
    height: 1200px;
    overflow: hidden;
    background: var(--ink);
  }
  .poster {
    position: relative;
    width: 809px;
    height: 1200px;
    overflow: hidden;
    background: var(--ink);
  }
  .poster-photo {
    position: absolute;
    inset: 0;
    background:
      radial-gradient(ellipse 30% 22% at 48% 22%, var(--haze) 0%, rgba(207,221,226,0.5) 55%, transparent 100%),
      radial-gradient(ellipse 45% 35% at 90% 55%, var(--glow) 0%, rgba(244,248,248,0.7) 50%, transparent 100%),
      radial-gradient(ellipse 20% 18% at 12% 62%, var(--glow) 0%, transparent 100%),
      radial-gradient(ellipse 18% 12% at 62% 82%, var(--ember) 0%, transparent 100%),
      linear-gradient(160deg, var(--steel) 0%, #3a4448 45%, var(--ink) 100%);
  }
  .shadow-band {
    position: absolute;
    inset: 0;
  }
  .title {
    position: absolute;
    left: 50%;
    top: 52%;
    margin: 0;
    transform: translate(-50%, -50%) rotate(-54deg);
    font-family: "Cinzel", serif;
    font-weight: 400;
    font-size: 60px;
    letter-spacing: 3px;
    color: var(--title);
    white-space: nowrap;
  }
</style>
</head>
<body>
  <main class="poster">
    <div class="poster-photo" role="img" aria-label="Blurred photograph of a domed hotel tower against a pale sky, with a dark silhouetted figure and warm-lit buildings below"></div>
    <svg class="shadow-band" width="809" height="1200" viewBox="0 0 809 1200" aria-hidden="true">
      <polygon points="700,0 809,0 809,120 330,1000 180,1000" fill="#0a0808" opacity="0.92"/>
      <polygon points="0,0 230,0 180,420 60,1200 0,1200" fill="#0a0808" opacity="0.85"/>
    </svg>
    <h1 class="title">Seven Quiet Rooms</h1>
  </main>
</body>
</html>
```